FLYER: Human Factors in Traffic Crashes - Analysis of Drivers' Responses - training

We are hosting a class in Australia 30, November to 4, December 2020. I would like to have a flyer designed to "sell" the class with description of course topics. I have uploaded a flyer I started on my own but I want it to be professional. Dr. Pelloway only gets to AU every 3-5 years to teach from the US. I would like to have some type of roadway scenery, prefer a nighttime scene.

Target Market(s)

Accident reconstructionists and engineers, police reconstructionists.

Font styles to use
Serif

Colors
fec214

Requirements
Must have
• Name of course and course topics, location of course, price, website and contact information.
Nice to have
• Some type of roadway background, possibly a nighttime scene on a roadway.

```html
<!DOCTYPE html>
<html lang="en">
<head>
<meta charset="utf-8">
<title>Human Factors in Traffic Crashes – Course Flyer</title>
<link href="https://fonts.googleapis.com/css2?family=Archivo+Black&family=Oswald:wght@500;600;700&family=Roboto+Condensed:wght@400;700&display=swap" rel="stylesheet">
<style>
  :root {
    --gold: #fec214;
    --red: #f01010;
    --white: #ffffff;
    --ink: #111111;
    --night: #0f1c33;
    --dusk: #2c3e5c;
    --amber: #f28a1c;
    --glow: #fde2a6;
    --page: #ffffff;
  }
  * { margin: 0; padding: 0; box-sizing: border-box; }
  html, body { width: 1200px; height: 1200px; overflow: hidden; background: var(--page); }
  .canvas { position: relative; width: 1200px; height: 1200px; }
  .flyer {
    position: absolute; left: 255px; top: 111px; width: 691px; height: 978px;
    overflow: hidden; font-family: "Roboto Condensed", sans-serif; color: var(--white);
  }
  .scenery {
    position: absolute; inset: 0;
    background:
      radial-gradient(ellipse 70% 30% at 20% 4%, rgba(120,170,210,.55), transparent 70%),
      radial-gradient(ellipse 90% 45% at 55% 100%, var(--glow), transparent 70%),
      linear-gradient(180deg, var(--dusk) 0%, var(--night) 22%, #1a1a22 42%, #5a3516 60%, var(--amber) 80%, #f7b356 100%);
  }
  .abs { position: absolute; }
  .brand { left: 37px; top: 44px; width: 300px; }
  .brand-name { font-family: "Archivo Black", sans-serif; font-size: 47px; line-height: 1; color: var(--ink); letter-spacing: 1px; }
  .brand-sub { font-family: "Archivo Black", sans-serif; font-size: 24px; line-height: 1.1; color: var(--ink); margin-top: 4px; }
  .brand-mark { display: block; width: 14px; height: 14px; background: var(--gold); margin-top: 8px; }

  .title { left: 31px; top: 172px; font-family: "Archivo Black", sans-serif; color: var(--gold); line-height: .98; }
  .title span { display: block; }
  .title .human { font-size: 74px; letter-spacing: 1px; }
  .title .factors { font-size: 74px; letter-spacing: 2px; }

  .subtitle { left: 33px; top: 303px; font-family: "Oswald", sans-serif; font-weight: 700; font-size: 38px; line-height: 48px; color: var(--red); }
  .presented { left: 33px; top: 455px; font-family: "Oswald", sans-serif; font-weight: 500; font-size: 24px; color: var(--gold); }
  .presenter { left: 33px; top: 490px; font-family: "Oswald", sans-serif; font-weight: 700; font-size: 33px; color: var(--gold); }
  .presenter small { font-size: 22px; }
  .credential { left: 33px; top: 533px; font-family: "Oswald", sans-serif; font-weight: 500; font-size: 17px; color: var(--gold); }

  .band { font-family: "Oswald", sans-serif; font-weight: 700; }
  .band svg { position: absolute; inset: 0; }
  .band span { position: relative; display: block; }
  .band-open { left: 0; top: 591px; width: 236px; height: 47px; color: var(--ink); font-size: 31px; }
  .band-open span { padding: 2px 0 0 33px; }
  .band-city { left: 28px; top: 645px; width: 284px; height: 47px; color: var(--white); font-size: 31px; }
  .band-city span { padding: 2px 0 0 55px; }
  .band-fee { left: 0; top: 737px; width: 300px; height: 48px; color: var(--red); font-size: 31px; }
  .band-fee span { padding: 2px 0 0 34px; }

  .price { left: 33px; font-family: "Oswald", sans-serif; font-weight: 700; font-size: 30px; color: var(--ink); }
  .price-au { top: 795px; }
  .price-usd { top: 839px; }
  .note { left: 33px; top: 883px; width: 340px; font-size: 16px; line-height: 21px; color: var(--ink); }

  .topics-head { right: 23px; top: 60px; text-align: right; font-family: "Oswald", sans-serif; font-weight: 700; font-size: 40px; line-height: 47px; color: var(--red); }
  .topics { right: 31px; top: 160px; width: 300px; list-style: none; text-align: right; font-size: 15.5px; line-height: 19.5px; }
  .topics li { margin-bottom: 10.5px; }

  .location { right: 30px; top: 695px; text-align: right; color: var(--ink); }
  .location-head { font-family: "Oswald", sans-serif; font-weight: 600; font-size: 25px; display: flex; justify-content: flex-end; align-items: flex-end; gap: 4px; }
  .location-head svg { width: 30px; height: 66px; }
  .location-lines { font-size: 15.5px; line-height: 20px; margin-top: 2px; }
  .divider { right: 30px; top: 811px; width: 250px; height: 1px; background: rgba(17,17,17,.45); }
  .contact { right: 26px; top: 818px; text-align: right; color: var(--ink); }
  .contact .register { font-size: 25px; line-height: 30px; }
  .contact .web { font-size: 18px; font-weight: 700; line-height: 22px; }
  .contact .or { font-size: 18px; line-height: 24px; }
  .contact .mail { font-size: 19px; line-height: 22px; }
  .contact .phone { font-family: "Oswald", sans-serif; font-weight: 700; font-size: 42px; line-height: 48px; }
</style>
</head>
<body>
<div class="canvas">
  <article class="flyer">
    <div class="scenery" role="img" aria-label="Night-time highway with streaking orange headlight trails under a starry sky"></div>

    <header class="abs brand">
      <div class="brand-name">ROADLINE</div>
      <div class="brand-sub">SAFETY GROUP</div>
      <i class="brand-mark"></i>
    </header>

    <h1 class="abs title"><span class="human">HUMAN</span><span class="factors">FACTORS</span></h1>
    <h2 class="abs subtitle">IN TRAFFIC CRASHES,<br>ANALYSIS OF DRIVERS’<br>RESPONSES</h2>
    <p class="abs presented">Presented by</p>
    <p class="abs presenter">JEFFERY PELLOWAY <small>Ph.D.</small></p>
    <p class="abs credential">WORLD RENOWNED HUMAN FACTORS EXPERT</p>

    <div class="abs band band-open">
      <svg viewBox="0 0 236 47" preserveAspectRatio="none"><polygon points="0,0 212,0 236,47 0,47" fill="#fff"/><polygon points="0,0 20,0 0,20" fill="#ddd"/></svg>
      <span>OPEN CLASS</span>
    </div>
    <div class="abs band band-city">
      <svg viewBox="0 0 284 47" preserveAspectRatio="none"><polygon points="0,0 256,0 284,47 22,47" fill="#f01010"/></svg>
      <span>MANLEY NSW</span>
    </div>
    <div class="abs band band-fee">
      <svg viewBox="0 0 300 48" preserveAspectRatio="none"><defs><linearGradient id="feeFade" x1="0" x2="1"><stop offset=".7" stop-color="#fff"/><stop offset="1" stop-color="#fff" stop-opacity="0"/></linearGradient></defs><rect width="300" height="48" fill="url(#feeFade)"/></svg>
      <span>COURSE FEE</span>
    </div>
    <p class="abs price price-au">$1,730 AU</p>
    <p class="abs price price-usd">$1,200 USD</p>
    <p class="abs note">It has been 3 years since Dr. Pelloway has come to AU to teach, don’t miss out on this year’s class.</p>

    <h3 class="abs topics-head">COURSE<br>TOPICS</h3>
    <ul class="abs topics">
      <li>Acceleration</li>
      <li>Research in IDRR</li>
      <li>Nighttime recognition</li>
      <li>Driver decision making</li>
      <li>Perception-Response Time</li>
      <li>Pedestrian walking speeds</li>
      <li>Headlight mapping demonstration and instruction</li>
      <li>Response to slow moving or stopped vehicles on multilane high speed roads</li>
      <li>Lateral acceleration (swerving) for cars, motorcycles, and commercial vehicles</li>
      <li>Forward and backward acceleration of cars, motorcycles and commercial vehicles</li>
      <li>Gap acceptance for left turns, right turns, and through movements for drivers, riders, and pedestrians</li>
      <li>Drivers’ responses to green and yellow traffic signals, deceleration choice, reaction time and probability of stopping</li>
    </ul>

    <section class="abs location">
      <div class="location-head">
        <span>Location</span>
        <svg viewBox="0 0 30 66"><path d="M15 2a13 13 0 0 1 13 13c0 10-13 49-13 49S2 25 2 15A13 13 0 0 1 15 2z" fill="#111"/><circle cx="15" cy="15" r="6" fill="#f4a640"/></svg>
      </div>
      <div class="location-lines">Harbourview Centre – Sydney Harbour<br>12 Coastal Point Road, Manley NSW</div>
    </section>
    <div class="abs divider"></div>
    <section class="abs contact">
      <div class="register">Register on our website</div>
      <div class="web">www.roadlinesafetygroup.com</div>
      <div class="or">or Contact:</div>
      <div class="mail">Dana@roadlinesafetygroup.com</div>
      <div class="phone">860-555-0142</div>
    </section>
  </article>
</div>
</body>
</html>
```